Bakery Business Cards

We are in need of business cards for our bakery business--something non-generic that reflects our business and will stand out. We are a wholesale bakery that primarily services in-store bakeries, casinos, schools, distributors, and fund-raising companies. The family business was founded in 1960. (www.marlowsovenworks.com)

```html
<!DOCTYPE html>
<html lang="en">
<head>
<meta charset="utf-8">
<title>Marlow's Ovenworks — Business Cards</title>
<link rel="stylesheet" href="https://fonts.googleapis.com/css2?family=Tinos:ital,wght@0,400;0,700;1,400&display=swap">
<style>
  :root {
    --backdrop: #7b7b7b;
    --card-white: #ffffff;
    --brand-blue: #0047ba;
    --accent-grey: #a9a9ab;
    --text-light: #ffffff;
  }
  html, body {
    margin: 0;
    padding: 0;
    width: 1133px;
    height: 1200px;
    overflow: hidden;
    background: var(--backdrop);
    font-family: "Tinos", "Times New Roman", serif;
  }
  .canvas {
    position: relative;
    width: 1133px;
    height: 1200px;
  }
  .card {
    position: absolute;
    overflow: hidden;
  }
  .card--front {
    left: 218px;
    top: 153px;
    width: 696px;
    height: 397px;
    background: var(--card-white);
  }
  .card--back {
    left: 201px;
    top: 640px;
    width: 713px;
    height: 407px;
    background: var(--brand-blue);
  }
  .front-swoosh {
    position: absolute;
    inset: 0;
  }
  .brand-lockup {
    position: absolute;
    left: 62px;
    top: 78px;
    display: flex;
    align-items: center;
    gap: 14px;
    color: var(--brand-blue);
  }
  .brand-lockup__dot {
    width: 26px;
    height: 26px;
    border-radius: 50%;
    background: var(--brand-blue);
    flex: none;
  }
  .brand-lockup__name {
    font-weight: 700;
    font-size: 40px;
    line-height: 1.05;
  }
  .contact {
    position: absolute;
    right: 40px;
    top: 250px;
    margin: 0;
    padding: 0;
    list-style: none;
    color: var(--text-light);
    font-size: 16.5px;
    line-height: 20px;
    text-align: right;
  }
  .contact__item {
    display: flex;
    justify-content: flex-end;
    align-items: flex-start;
    gap: 12px;
  }
  .contact__item--address { margin-bottom: 13px; }
  .contact__icon {
    width: 14px;
    height: 14px;
    flex: none;
    margin-top: 3px;
    fill: var(--text-light);
  }
  .back-mark {
    position: absolute;
    left: 0;
    right: 0;
    top: 105px;
    display: flex;
    flex-direction: column;
    align-items: center;
    gap: 16px;
    color: var(--text-light);
  }
  .back-mark__dot {
    width: 72px;
    height: 72px;
    border-radius: 50%;
    background: var(--text-light);
  }
  .back-mark__name {
    font-weight: 700;
    font-size: 42px;
  }
  .tagline {
    position: absolute;
    left: 0;
    right: 0;
    top: 316px;
    text-align: center;
    color: var(--text-light);
  }
  .tagline__main {
    margin: 0;
    font-weight: 700;
    font-size: 24px;
    line-height: 30px;
  }
  .tagline__products {
    margin: 0;
    font-style: italic;
    font-size: 20px;
    line-height: 26px;
  }
</style>
</head>
<body>
<main class="canvas">

  <section class="card card--front" aria-label="Business card front">
    <svg class="front-swoosh" viewBox="0 0 696 397" width="696" height="397" aria-hidden="true">
      <path fill="var(--accent-grey)" d="M258 397 C310 290 430 228 560 158 C640 114 688 58 696 0 L696 397 Z"/>
      <path fill="var(--brand-blue)" stroke="var(--card-white)" stroke-width="2.5"
            d="M253 399 C300 300 420 240 560 172 C640 132 680 102 698 68 L698 399 Z"/>
    </svg>

    <div class="brand-lockup">
      <span class="brand-lockup__dot"></span>
      <span class="brand-lockup__name">Marlow's<br>Ovenworks</span>
    </div>

    <ul class="contact">
      <li class="contact__item contact__item--address">
        <span>5316 Birchwood Ave<br>Millbrook, OK 73120</span>
        <svg class="contact__icon" viewBox="0 0 14 14" aria-hidden="true"><path d="M7 0a5 5 0 0 0-5 5c0 3.6 5 9 5 9s5-5.4 5-9a5 5 0 0 0-5-5zm0 7a2 2 0 1 1 0-4 2 2 0 0 1 0 4z"/></svg>
      </li>
      <li class="contact__item">
        <span>(405) 555-0148</span>
        <svg class="contact__icon" viewBox="0 0 14 14" aria-hidden="true"><path d="M3 0.5l2.2 2.8-1.3 1.7c.9 1.9 2.4 3.4 4.3 4.3l1.7-1.3L12.7 10 11.4 12.8C6 12.4 1.6 8 1.2 2.6z"/></svg>
      </li>
      <li class="contact__item">
        <span>sales@marlowsovenworks.com</span>
        <svg class="contact__icon" viewBox="0 0 14 14" aria-hidden="true"><path d="M1 3h12v8H1z M1.5 3.5 7 8l5.5-4.5" stroke="var(--brand-blue)" stroke-width="1"/></svg>
      </li>
      <li class="contact__item">
        <span>marlowsovenworks.com</span>
        <svg class="contact__icon" viewBox="0 0 14 14" aria-hidden="true"><circle cx="7" cy="7" r="6.5"/><path d="M3 5c1.5-.5 2.5.5 2 2s1 2 .5 4M8 2c.5 1.5 2.5 1.5 3 3.5s-1.5 2-1 4" fill="none" stroke="var(--brand-blue)" stroke-width="1.2"/></svg>
      </li>
    </ul>
  </section>

  <section class="card card--back" aria-label="Business card back">
    <div class="back-mark">
      <span class="back-mark__dot"></span>
      <span class="back-mark__name">Marlow's Ovenworks</span>
    </div>
    <div class="tagline">
      <p class="tagline__main">Serving Sweetness Since 1960</p>
      <p class="tagline__products">Cobblers&nbsp; | &nbsp;Pies&nbsp; | &nbsp;Cookies</p>
    </div>
  </section>

</main>
</body>
</html>
```